ZESTMUNCHY
Zestmunchy is a food van, serving high vibe delicious food to go. This business is dedicated to healthy delicious feel good food, beauty in service and a sustainable planet.

The van will operate in the south west of western Australia at music festivals events markets wherever people need great food to go!

I like the idea of vibrant green mixed with a yellow?? background with some rays like the sun through the background.
The font needs to say vibrant energetic
TO ME -vibrant energetic font has to appear to be on the move - perhaps with shading??

I like fusha if that works for font? but the colour has to say food too.

I would like a symbol on the card a simple V turned into a womans raised arms. This should be vibrant too.
Thank you
Blessings
Marisol

Target Market(s)

target lovers of healthy high vibe food. music festival goers. age 18- 50 feel. audiance conscious eaters of feel great food

Industry/Entity Type

Events

Contact Information for Business Card

ZESTMUNCHY
High Vibe Food
Van
Marisol -owner/opperator
0458170396
Face book symbol - ZESTMUNCHY

on the I would like a logo of a simple V turned into a womans arms up toward the sky flip side

My number and name again
Zestmunchy- feel great mobile food
Festivals, events, markets & where high vibe food 2 go is appreciated

Requirements
Nice to have
• Moving energetic font
colour that says high vibe and healthy food

a logo that is a simple V turned into a woman's raised arms in gratitude

```html
<!DOCTYPE html>
<html lang="en">
<head>
<meta charset="utf-8">
<title>Zestmunchy – Business Card</title>
<link href="https://fonts.googleapis.com/css2?family=Questrial&family=Montserrat:wght@500;700&display=swap" rel="stylesheet">
<style>
  :root {
    --page: #e9e9e7;
    --green-light: #3f9a34;
    --green-mid: #2c8430;
    --green-deep: #1b6a2a;
    --yellow: #f4ea16;
    --yellow-line: #e8e21a;
    --ink-green: #2a8a2c;
    --white: #ffffff;
  }
  * { margin: 0; padding: 0; box-sizing: border-box; }
  html, body { width: 1200px; height: 1000px; overflow: hidden; }
  body {
    background: var(--page);
    font-family: "Questrial", sans-serif;
    position: relative;
  }
  .card {
    position: absolute;
    width: 520px;
    height: 316px;
    border-radius: 18px;
    overflow: hidden;
    box-shadow: 0 6px 14px rgba(0,0,0,0.18);
  }
  .green-field {
    background:
      repeating-linear-gradient(100deg, rgba(255,255,255,0.05) 0 22px, rgba(255,255,255,0) 22px 48px),
      radial-gradient(ellipse at 35% 0%, rgba(140,200,90,0.45), rgba(0,0,0,0) 60%),
      linear-gradient(160deg, var(--green-light), var(--green-mid) 45%, var(--green-deep));
  }

  /* Front */
  .card-front { left: 70px; top: 170px; }
  .front-title-row {
    position: absolute; left: 0; right: 0; top: 120px;
    display: flex; align-items: flex-end;
  }
  .front-title-row .row-space { flex: 1; }
  .front-name {
    font-family: "Questrial", sans-serif;
    font-size: 46px; line-height: 1; letter-spacing: 1px;
    color: var(--yellow);
    padding: 0 10px;
  }
  .front-title-row .row-rule {
    flex: 1; height: 2px; background: var(--yellow-line); margin-bottom: 4px;
  }
  .front-tag-row {
    position: absolute; left: 0; right: 0; top: 180px;
    display: flex; align-items: center;
  }
  .front-tag-row .row-rule { flex: 1; height: 2px; background: var(--yellow-line); }
  .front-tag-row .row-space { flex: 1; }
  .front-tagline {
    font-family: "Montserrat", sans-serif; font-weight: 500;
    font-size: 13px; color: var(--white);
    padding: 0 10px;
  }

  /* Back */
  .card-back { left: 610px; top: 520px; display: flex; }
  .back-identity { position: relative; width: 270px; height: 100%; }
  .back-name {
    position: absolute; left: 30px; top: 40px;
    font-size: 26px; color: var(--yellow); letter-spacing: 0.5px;
  }
  .back-person {
    position: absolute; left: 52px; top: 150px;
    font-family: "Montserrat", sans-serif; color: var(--white);
  }
  .back-person .person-name { font-weight: 700; font-size: 21px; letter-spacing: 0.5px; }
  .back-person .person-role { font-weight: 500; font-size: 13px; margin-top: 2px; }
  .back-person .person-phone { font-weight: 500; font-size: 16px; margin-top: 22px; letter-spacing: 1.5px; }
  .back-message {
    flex: 1; background: var(--yellow);
    display: flex; align-items: center; justify-content: center;
    padding: 0 28px 60px;
  }
  .back-message p {
    text-align: center; color: var(--ink-green);
    font-family: "Montserrat", sans-serif; font-weight: 500;
    font-size: 15px; line-height: 1.3;
  }
</style>
</head>
<body>
  <section class="card card-front green-field">
    <div class="front-title-row">
      <span class="row-space"></span>
      <span class="front-name">ZESTMUNCHY</span>
      <span class="row-rule"></span>
    </div>
    <div class="front-tag-row">
      <span class="row-rule"></span>
      <span class="front-tagline">Healthy Eats On Wheels</span>
      <span class="row-space"></span>
    </div>
  </section>

  <section class="card card-back">
    <div class="back-identity green-field">
      <div class="back-name">ZESTMUNCHY</div>
      <div class="back-person">
        <div class="person-name">MARISOL</div>
        <div class="person-role">Owner/Operator</div>
        <div class="person-phone">0458170396</div>
      </div>
    </div>
    <div class="back-message">
      <p>Fresh feel-good meals for gigs, fairs, markets &amp; anywhere tasty food on the go is loved.</p>
    </div>
  </section>
</body>
</html>
```